Ciel doux

Hello,
I’m a designer sunglasses reatail Store owner in Montreal, Quebec.

Looking for something modern, fresh with a trendy appeal.

Will send my logo.
Thank you.

Store

```html
<!DOCTYPE html>
<html lang="fr">
<head>
<meta charset="utf-8">
<title>Ciel doux — cartes de visite</title>
<link rel="stylesheet" href="https://fonts.googleapis.com/css2?family=Nunito+Sans:wght@400;600;700&family=Mrs+Saint+Delafield&display=swap">
<style>
  :root {
    --page: #e4e4e4;
    --card: #f6f6f5;
    --ink: #2b2b2b;
    --ink-soft: #444444;
    --frame-dark: #2e2f30;
    --lens-grey: #6d726b;
    --lens-blue: #5fb8ea;
    --lens-blue-light: #bfe4f7;
    --white: #ffffff;
  }
  * { margin: 0; padding: 0; box-sizing: border-box; }
  html, body {
    width: 1200px;
    height: 1050px;
    overflow: hidden;
    background: var(--page);
    font-family: "Nunito Sans", Arial, sans-serif;
    color: var(--ink);
  }
  .sheet {
    position: relative;
    width: 1200px;
    height: 1050px;
    display: flex;
    flex-direction: column;
    align-items: center;
    justify-content: center;
    gap: 40px;
  }
  .card {
    position: relative;
    width: 880px;
    height: 470px;
    background: var(--card);
    overflow: hidden;
  }
  .brand-name {
    font-family: "Nunito Sans", Arial, sans-serif;
    font-weight: 700;
    color: var(--ink);
    letter-spacing: 0.5px;
  }

  /* Front */
  .card-front .brand-name {
    position: absolute;
    left: 54px;
    top: 36px;
    font-size: 40px;
  }
  .contact {
    position: absolute;
    left: 54px;
    top: 148px;
    font-size: 18px;
    line-height: 24px;
    color: var(--ink-soft);
  }
  .contact .address { margin-bottom: 30px; }
  .product-photo {
    position: absolute;
    left: 0;
    top: 0;
    width: 880px;
    height: 470px;
  }
  .signature-name {
    position: absolute;
    left: 430px;
    top: 236px;
    font-family: "Mrs Saint Delafield", cursive;
    font-size: 54px;
    color: var(--white);
    transform: rotate(-12deg);
    transform-origin: left center;
    white-space: nowrap;
  }
  .role {
    position: absolute;
    left: 752px;
    top: 318px;
    font-size: 19px;
    font-weight: 600;
    color: var(--white);
  }

  /* Back */
  .card-back .eyewear-photo {
    position: absolute;
    left: 167px;
    top: 90px;
    width: 546px;
    height: 180px;
  }
  .card-back .brand-name {
    position: absolute;
    left: 0;
    right: 0;
    top: 336px;
    text-align: center;
    font-size: 40px;
  }
  .card-back .website {
    position: absolute;
    left: 0;
    right: 0;
    top: 402px;
    text-align: center;
    font-size: 19px;
    color: var(--ink-soft);
  }
</style>
</head>
<body>
<main class="sheet">

  <section class="card card-front">
    <svg class="product-photo" viewBox="0 0 880 470" role="img" aria-label="Photo en gros plan d'une paire de lunettes de soleil noires aux verres gris-vert">
      <defs>
        <linearGradient id="frontPhotoTone" x1="0" y1="1" x2="1" y2="0">
          <stop offset="0" stop-color="var(--frame-dark)"/>
          <stop offset="0.55" stop-color="var(--lens-grey)"/>
          <stop offset="1" stop-color="#8a8f88"/>
        </linearGradient>
      </defs>
      <path d="M0 408 C 200 330, 480 196, 880 150 L 880 470 L 0 470 Z" fill="url(#frontPhotoTone)"/>
    </svg>

    <div class="brand-name">Ciel doux</div>

    <div class="contact">
      <p class="address">Atelier 12, 480 rue Laurier<br>Montréal, H2T 1K9</p>
      <p class="phone">+1 0000-555-214</p>
      <p class="email">emarchand@cieldoux.ca</p>
      <p class="website">www.cieldoux.ca</p>
    </div>

    <div class="signature-name">Élise Marchand</div>
    <div class="role">Designer</div>
  </section>

  <section class="card card-back">
    <svg class="eyewear-photo" viewBox="0 0 546 180" role="img" aria-label="Photo de lunettes de soleil rondes à monture argentée et verres bleus miroir">
      <defs>
        <linearGradient id="backPhotoTone" x1="0" y1="0" x2="0" y2="1">
          <stop offset="0" stop-color="var(--lens-blue-light)"/>
          <stop offset="1" stop-color="var(--lens-blue)"/>
        </linearGradient>
      </defs>
      <rect x="0" y="0" width="546" height="180" rx="90" fill="url(#backPhotoTone)"/>
    </svg>

    <div class="brand-name">Ciel doux</div>
    <div class="website">www.CielDoux.ca</div>
  </section>

</main>
</body>
</html>
```